The Perfect Business Card for PineHarbor

I am looking for a business card which beautifully incorporates my logo, reflects my business and looks special, elegant and clean.

```html
<!DOCTYPE html>
<html lang="en">
<head>
<meta charset="utf-8">
<title>PineHarbor Business Card</title>
<link href="https://fonts.googleapis.com/css2?family=Cinzel:wght@400&family=EB+Garamond:wght@400&display=swap" rel="stylesheet">
<style>
  :root {
    --backdrop: #e8e3db;
    --card: #232222;
    --card-edge: #2b2a2a;
    --green: #6a9a2e;
    --text-light: #e9e9e6;
    --mark-grey: #55565a;
    --icon-green: #5e8c2a;
  }
  * { margin: 0; padding: 0; box-sizing: border-box; }
  html, body {
    width: 1200px; height: 900px; overflow: hidden;
    background: var(--backdrop);
  }
  .canvas { position: relative; width: 1200px; height: 900px; }
  .card {
    position: absolute;
    width: 660px; height: 378px;
    background: linear-gradient(160deg, var(--card-edge), var(--card));
    border-radius: 42px;
    box-shadow: 0 14px 30px rgba(0,0,0,0.22);
    overflow: hidden;
  }
  .card--front { left: 90px; top: 50px; }
  .card--back { left: 450px; top: 472px; }

  .decor-ring {
    position: absolute;
    border: 4px solid var(--mark-grey);
    border-radius: 50%;
    opacity: 0.85;
  }
  .card--front .decor-ring { left: 60px; top: 95px; width: 250px; height: 250px; }
  .card--back .decor-ring { left: 80px; top: 120px; width: 220px; height: 220px; }

  .brand-name {
    position: absolute;
    font-family: "Cinzel", "Times New Roman", serif;
    font-weight: 400;
    color: var(--green);
    letter-spacing: 1px;
    line-height: 1;
  }
  .card--front .brand-name { left: 255px; top: 170px; font-size: 50px; }

  .holder { position: absolute; left: 42px; top: 46px; }
  .holder__role {
    font-family: "EB Garamond", Georgia, serif;
    color: var(--text-light);
    font-size: 21px;
    line-height: 1.1;
  }
  .holder__name {
    font-family: "Cinzel", "Times New Roman", serif;
    color: var(--green);
    font-size: 26px;
    line-height: 1.1;
    letter-spacing: 1px;
  }

  .contact-list {
    position: absolute; left: 340px; top: 60px;
    list-style: none;
    font-family: "EB Garamond", Georgia, serif;
    color: var(--text-light);
    font-size: 17px;
  }
  .contact-list li {
    display: flex; align-items: center; gap: 10px;
    height: 29px;
  }
  .contact-list svg { width: 15px; height: 15px; flex: none; fill: var(--icon-green); }

  .divider {
    position: absolute; left: 320px; top: 196px;
    width: 340px; height: 2px;
    background: var(--green);
  }

  .brand-lockup {
    position: absolute; left: 330px; top: 232px;
    display: flex; align-items: center; gap: 14px;
  }
  .brand-lockup__dot {
    width: 40px; height: 40px;
    border: 3px solid var(--green);
    border-radius: 50%;
  }
  .brand-lockup .brand-name { position: static; font-size: 34px; }
</style>
</head>
<body>
<main class="canvas">

  <section class="card card--front" aria-label="Card front">
    <div class="decor-ring" aria-hidden="true"></div>
    <h1 class="brand-name">PINEHARBOR</h1>
  </section>

  <section class="card card--back" aria-label="Card back">
    <div class="holder">
      <p class="holder__role">Director</p>
      <p class="holder__name">DANIEL HART</p>
    </div>

    <div class="decor-ring" aria-hidden="true"></div>

    <ul class="contact-list">
      <li>
        <svg viewBox="0 0 16 16" aria-hidden="true"><path d="M3 2l3 0 1 3-2 1.5c1 2 2.5 3.5 4.5 4.5L11 9l3 1v3c0 .6-.4 1-1 1C7.5 14 2 8.5 2 3c0-.6.4-1 1-1z"/></svg>
        (00) 0000 0000
      </li>
      <li>
        <svg viewBox="0 0 16 16" aria-hidden="true"><path d="M1 4h14v9H1z M1 4l7 5 7-5" fill="none" stroke="#5e8c2a" stroke-width="1.6"/></svg>
        daniel@pineharbor.com
      </li>
      <li>
        <svg viewBox="0 0 16 16" aria-hidden="true"><circle cx="8" cy="8" r="6.5" fill="none" stroke="#5e8c2a" stroke-width="1.5"/><path d="M1.5 8h13M8 1.5c-3 3.5-3 9.5 0 13M8 1.5c3 3.5 3 9.5 0 13" fill="none" stroke="#5e8c2a" stroke-width="1.2"/></svg>
        www.pineharbor.com
      </li>
      <li>
        <svg viewBox="0 0 16 16" aria-hidden="true"><path d="M8 1a5 5 0 0 1 5 5c0 4-5 9-5 9S3 10 3 6a5 5 0 0 1 5-5zm0 3a2 2 0 1 0 0 4 2 2 0 0 0 0-4z"/></svg>
        00 dummy city, dummy place
      </li>
    </ul>

    <div class="divider" aria-hidden="true"></div>

    <div class="brand-lockup">
      <span class="brand-lockup__dot" aria-hidden="true"></span>
      <span class="brand-name">PINEHARBOR</span>
    </div>
  </section>

</main>
</body>
</html>
```